Quorvix Letter head

Quorvix is a young and energetic software development consultancy. We spend our time working with clients to turn what ever is in their heads in to software.
We are trying to create an image of a high class software boutique who build class leading bespoke solutions.
We need a sharp letter head that looks great on high quality media.
We like bold colours and distinctive design. So show us what you can do.
Industry/Entity Type
Software
Requirements
Must have
- Our company is based in the UK and are requried to have on the paper somewhere the following information:
* Registered company name: Quorvix Ltd
* Registered company number
* VAT registration number
In addition we also want the following:
* An email address
* Telephone number
* Website address
An example of what some pages have in their footer is something like the following:
Quorvix Ltd is registered in England and Wales. Reg. no: 5316274
Registered office: 48 Cobblewick Road, Harlow Essex, CM93TP. Tel: 07712365081
You do not have to use this sentance but please make sure your design incorporates accommodates the requirements for UK based companies

```html
<!DOCTYPE html>
<html lang="en">
<head>
<meta charset="utf-8">
<title>Quorvix Letterhead</title>
<link rel="stylesheet" href="https://fonts.googleapis.com/css2?family=Montserrat:wght@300;400&display=swap">
<style>
  :root {
    --brand-red: #c21d2d;
    --paper: #ffffff;
    --backdrop: #e7eaeb;
    --ink: #3a3a3a;
    --ink-soft: #a9a9a9;
    --monogram-tint: #f6f6f6;
    --white: #ffffff;
  }
  * { margin: 0; padding: 0; box-sizing: border-box; }
  html, body { width: 1200px; height: 791px; overflow: hidden; }
  body {
    background: var(--backdrop);
    font-family: "Montserrat", "Helvetica Neue", Arial, sans-serif;
    position: relative;
  }
  .letterhead {
    position: absolute;
    left: 169px; top: 123px;
    width: 400px; height: 543px;
    background: var(--paper);
    border-radius: 10px;
    overflow: hidden;
    color: var(--ink);
  }
  .letterhead__monogram {
    position: absolute; inset: 0;
    background: linear-gradient(160deg, var(--paper) 0%, var(--monogram-tint) 50%, var(--paper) 100%);
  }
  .accent-bar {
    position: absolute;
    width: 3px;
    background: var(--brand-red);
  }
  .accent-bar--left { left: 0; top: 70px; height: 28px; }
  .accent-bar--right { right: 0; top: 70px; height: 60px; }
  .wordmark {
    position: absolute;
    left: 38px; top: 40px;
    font-size: 24px;
    font-weight: 400;
    letter-spacing: 0.5px;
    color: var(--brand-red);
    line-height: 1;
  }
  .registration {
    position: absolute;
    left: 38px; top: 69px;
    font-size: 7.5px;
    font-weight: 300;
    line-height: 9.6px;
    color: var(--ink-soft);
  }
  .contact {
    position: absolute;
    left: 269px; top: 69px;
    font-size: 7.5px;
    font-weight: 300;
    line-height: 9.6px;
    color: var(--ink-soft);
    list-style: none;
  }
  .contact li { margin-bottom: 5px; }
  .contact li:first-child { margin-bottom: 5px; }
  .letter-body {
    position: absolute;
    left: 38px; top: 148px;
    width: 330px;
    font-size: 8.2px;
    font-weight: 400;
    line-height: 10.8px;
    color: var(--ink);
  }
  .letter-body p { margin-bottom: 10.8px; white-space: nowrap; }
  .signature {
    position: absolute;
    left: 39px; top: 470px;
  }
  .signature__name { font-size: 16px; font-weight: 400; line-height: 1; }
  .signature__role { font-size: 7.5px; font-weight: 400; margin-top: 2px; }
  .folder {
    position: absolute;
    left: 631px; top: 123px;
    width: 399px; height: 543px;
  }
  .folder svg { position: absolute; inset: 0; }
  .folder__wordmark {
    position: absolute;
    left: 0; right: 0; top: 254px;
    text-align: center;
    font-size: 34px;
    font-weight: 400;
    letter-spacing: 1px;
    color: var(--white);
    line-height: 1;
  }
</style>
</head>
<body>
  <section class="letterhead" aria-label="Quorvix letterhead">
    <div class="letterhead__monogram" role="img" aria-label="Faint large monogram pattern across the paper"></div>
    <span class="accent-bar accent-bar--left"></span>
    <span class="accent-bar accent-bar--right"></span>
    <div class="wordmark">QUORVIX</div>
    <p class="registration">Quorvix Ltd is registered in<br>England and Wales.<br>Reg. no: 5316274</p>
    <ul class="contact">
      <li>48 Cobblewick Road,<br>Harlow Essex, CM93TP</li>
      <li>Tel: 07712365081</li>
      <li>hello@quorvix.example</li>
      <li>www.quorvix.example</li>
    </ul>
    <div class="letter-body">
      <p>Lorem Ipsum,</p>
      <p>Cras mattis consectetur purus sit amet fermentum. Etiam porta sem malesuada<br>magna mollis euismod. Integer posuere erat a ante venenatis dapibus posuere<br>velit aliquet. Cras justo odio, dapibus ac facilisis in, egestas eget quam. Aenean<br>eu leo quam. Pellentesque ornare sem lacinia quam venenatis vestibulum.</p>
      <p>Vivamus sagittis lacus vel augue laoreet rutrum faucibus dolor auctor. Donec sed<br>odio dui. Etiam porta sem malesuada magna mollis euismod. Morbi leo risus,<br>porta ac consectetur ac, vestibulum at eros. Nullam id dolor id nibh ultricies<br>vehicula ut id elit.</p>
      <p>Donec id elit non mi porta gravida at eget metus. Fusce dapibus, tellus ac cursus<br>commodo, tortor mauris condimentum nibh, ut fermentum massa justo sit amet<br>risus. Cras justo odio, dapibus ac facilisis in, egestas eget quam. Cum sociis<br>natoque penatibus et magnis dis parturient montes, nascetur ridiculus mus.</p>
      <p>Cum sociis natoque penatibus et magnis dis parturient montes, nascetur ridicu-<br>lus mus. Curabitur blandit tempus porttitor. Aenean lacinia bibendum nulla sed<br>consectetur. Lorem ipsum dolor sit amet, consectetur adipiscing elit.</p>
      <p>Cras justo odio, dapibus ac facilisis in, egestas eget quam. Morbi leo risus, porta<br>ac consectetur ac, vestibulum at eros. Duis mollis, est non commodo luctus, nisi<br>erat porttitor ligula, eget lacinia odio sem nec elit. Integer posuere erat a ante<br>venenatis dapibus posuere velit aliquet. Vivamus sagittis lacus vel augue laoreet<br>rutrum faucibus dolor auctor.</p>
    </div>
    <div class="signature">
      <div class="signature__name">Your Name</div>
      <div class="signature__role">Company Director</div>
    </div>
  </section>

  <section class="folder" aria-label="Quorvix presentation folder">
    <svg width="399" height="543" viewBox="0 0 399 543" aria-hidden="true">
      <path fill="var(--brand-red)" d="M10 0 H389 Q399 0 399 10 V115 Q399 124 390 128 L378 133 Q372 136 372 143 V244 Q372 251 378 254 L390 259 Q399 263 399 272 V533 Q399 543 389 543 H10 Q0 543 0 533 V10 Q0 0 10 0 Z"/>
    </svg>
    <div class="folder__wordmark">QUORVIX</div>
  </section>
</body>
</html>
```